The Reefside Clinic PowerPoint Design

We are looking for a new PowerPoint template design to reflect our branding and to be used for presentations at international conferences and online conferences. An example of our current template which is outdated is attached. We would like to still have a blue colour background as this represents water (but the exact background can be modified). We would like a professional, modern, and sharp feel to the templates. The template should include an Intro Slide, content slide, and closing/questions slide. The template needs to be prepared for both the standards, the 4:3 and Wide screen 16:9. Logos and branding in the attached power point can be used. Please visit our website www.thereefsideclinic.com to see more about the company.

```html
<!DOCTYPE html>
<html lang="en">
<head>
<meta charset="utf-8">
<title>The Reefside Clinic – Intro Slide</title>
<link rel="stylesheet" href="https://fonts.googleapis.com/css2?family=Montserrat:wght@400;500;700;800&display=swap">
<style>
  :root {
    --ink-black: #000000;
    --deep-blue: #0a3f8f;
    --ocean-blue: #1466c4;
    --surface-blue: #4fb3f0;
    --band-cyan: #00b4d0;
    --band-navy: #0b56ad;
    --accent-sky: #14a3e6;
    --paper: #ffffff;
    --badge-green: #7cbb43;
  }
  * { margin: 0; padding: 0; box-sizing: border-box; }
  html, body {
    width: 1200px; height: 687px; overflow: hidden;
    background: var(--paper);
    font-family: "Montserrat", sans-serif;
  }
  .slide {
    position: relative; width: 1200px; height: 687px; overflow: hidden;
    background: var(--ink-black);
  }
  .ocean-photo {
    position: absolute; left: 0; top: 0; width: 820px; height: 540px;
    background:
      radial-gradient(ellipse 320px 220px at 360px 40px, rgba(140,215,255,0.85), rgba(140,215,255,0) 70%),
      linear-gradient(90deg, var(--ocean-blue) 0%, var(--deep-blue) 60%, var(--ink-black) 100%);
  }
  .wave { position: absolute; left: 0; top: 0; width: 1200px; height: 687px; }
  .title-block {
    position: absolute; left: 580px; width: 600px; top: 132px;
    text-align: center; color: var(--paper);
  }
  .title-welcome { font-weight: 500; font-size: 62px; line-height: 1; letter-spacing: -0.5px; }
  .title-name { font-weight: 800; font-size: 53px; line-height: 1; margin-top: 10px; letter-spacing: 0.5px; }
  .presenter {
    margin-top: 36px; font-weight: 500; font-size: 26px; color: var(--accent-sky);
  }
  .event-date {
    margin-top: 56px; font-weight: 500; font-size: 20px;
    display: flex; justify-content: center; align-items: center; gap: 18px;
  }
  .event-date .dot { width: 14px; height: 14px; border-radius: 50%; background: var(--accent-sky); }
  .brand-name {
    position: absolute; left: 150px; top: 572px;
    display: flex; align-items: center; gap: 12px;
    font-weight: 700; font-size: 40px; color: var(--accent-sky); letter-spacing: -0.5px;
  }
  .brand-name .mark { width: 10px; height: 10px; border-radius: 50%; background: var(--accent-sky); }
  .partner-badge {
    position: absolute; left: 975px; top: 584px; width: 173px; height: 60px;
    background: var(--badge-green);
  }
</style>
</head>
<body>
  <main class="slide">
    <div class="ocean-photo" role="img" aria-label="Underwater photo looking up at a school of sharks silhouetted against the sunlit surface"></div>

    <svg class="wave" viewBox="0 0 1200 687" aria-hidden="true">
      <path fill="var(--band-cyan)" d="M0,442 C160,425 360,430 620,478 C820,515 1000,495 1200,402 L1200,687 L0,687 Z"/>
      <path fill="var(--band-navy)" d="M0,455 C160,440 360,445 620,492 C820,528 1000,510 1200,428 L1200,687 L0,687 Z"/>
      <path fill="var(--paper)" d="M0,512 C160,465 360,460 620,505 C820,540 1000,535 1200,462 L1200,687 L0,687 Z"/>
    </svg>

    <section class="title-block">
      <h1 class="title-welcome">Welcome to</h1>
      <h2 class="title-name">REEFSIDE CLINIC</h2>
      <p class="presenter">Dr. Name of the Doctor</p>
      <p class="event-date"><span class="dot"></span>Monday 30th July 2020<span class="dot"></span></p>
    </section>

    <div class="brand-name">The Reefside Clinic<span class="mark"></span></div>
    <div class="partner-badge" role="img" aria-label="Partner badge"></div>
  </main>
</body>
</html>
```